I need a simple, classy and stylish business card. I would like it to have a black background with white writing. I would like you to use my logo you designed on the front with the word 'Imagery" used underneath it in the same font. On the back I was thinking of the website at the top 'tormavine.com' Then my social media accounts, Can you use the instagram, Facebook and twitter logo then my handles?
Please let me know what you think.
Regards Lars
Industry/Entity Type
Business
Requirements
Must have
- Website: www.tormavine.com
- Social media handles..
- Instagram: @Lars_Tormavine_Imagery
- Facebook: Lars Tormavine Imagery
- Twitter: @Lars_Tormavin
- Email: info@tormavin.com
- Phone: 0473 518 609

```html
<!DOCTYPE html>
<html lang="en">
<head>
<meta charset="utf-8">
<title>Lars Tormavine Imagery – Business Card</title>
<link href="https://fonts.googleapis.com/css2?family=Indie+Flower&display=swap" rel="stylesheet">
<style>
  :root {
    --backdrop: #3a3a3a;
    --card: #1f1f1f;
    --card-edge: #2b2b2b;
    --ink: #f2f2f2;
    --ink-soft: #cfcfcf;
    --mark: #e9e9e9;
  }
  * { margin: 0; padding: 0; box-sizing: border-box; }
  html, body {
    width: 1200px; height: 873px; overflow: hidden;
    background: var(--backdrop);
  }
  .stage {
    position: relative; width: 1200px; height: 873px;
    display: flex; align-items: center; justify-content: center; gap: 40px;
  }
  .card {
    width: 540px; height: 310px;
    background: var(--card);
    border: 1px solid var(--card-edge);
    border-radius: 18px;
    box-shadow: 0 18px 40px rgba(0,0,0,.45);
    font-family: "Indie Flower", cursive;
    color: var(--ink);
    position: relative;
  }
  /* Front */
  .card-front { display: flex; align-items: center; justify-content: center; gap: 26px; }
  .brand-dot {
    width: 92px; height: 92px; border-radius: 50%;
    border: 4px solid var(--mark);
  }
  .brand-name { display: flex; flex-direction: column; line-height: 1; }
  .brand-name .name { font-size: 50px; }
  .brand-name .tagline { font-size: 50px; padding-left: 60px; margin-top: 6px; }
  /* Back */
  .card-back { display: flex; flex-direction: column; align-items: center; padding-top: 26px; }
  .website { font-size: 30px; letter-spacing: 1px; }
  .contacts { list-style: none; margin-top: 12px; align-self: flex-start; padding-left: 175px; }
  .contacts li {
    display: flex; align-items: center; gap: 10px;
    height: 38px; font-size: 17px; color: var(--ink-soft);
  }
  .contact-icon {
    width: 28px; height: 28px; flex: none;
    display: flex; align-items: center; justify-content: center;
  }
  .icon-round { border-radius: 50%; background: var(--ink-soft); width: 26px; height: 26px; }
  .icon-square { border-radius: 6px; background: var(--ink-soft); width: 26px; height: 26px; }
  .phone { font-size: 34px; margin-top: 18px; }
</style>
</head>
<body>
<main class="stage">
  <section class="card card-front" aria-label="Card front">
    <span class="brand-dot" aria-hidden="true"></span>
    <div class="brand-name">
      <span class="name">Lars Tormavine</span>
      <span class="tagline">Imagery</span>
    </div>
  </section>

  <section class="card card-back" aria-label="Card back">
    <p class="website">www.tormavine.com</p>
    <ul class="contacts">
      <li><span class="contact-icon"><span class="icon-square"></span></span>: @Lars_Tormavine_Imagery</li>
      <li><span class="contact-icon"><span class="icon-round"></span></span>: Lars Tormavine Imagery</li>
      <li><span class="contact-icon"><span class="icon-round"></span></span>: @Lars_Tormavin</li>
      <li>
        <span class="contact-icon">
          <svg width="28" height="20" viewBox="0 0 28 20" aria-hidden="true">
            <rect x="1" y="1" width="26" height="18" rx="2" fill="#e6e6e6" stroke="#9a9a9a"/>
            <path d="M1 2 L14 12 L27 2" fill="none" stroke="#555" stroke-width="1.5"/>
          </svg>
        </span>: info@tormavin.com
      </li>
    </ul>
    <p class="phone">Call us: 0473 518 609</p>
  </section>
</main>
</body>
</html>
```